Australian IT Company New Logo Business Cards Required

We are a computer consultancy / MSP located in Brisbane Australia looking to have business cards designed with our new logo, we are looking for something professional that catches the eye.
I can provide the logo in other formats if required, let's see what you can create!

```html
<!DOCTYPE html>
<html lang="en">
<head>
<meta charset="utf-8">
<title>Norvane Business Cards</title>
<link rel="stylesheet" href="https://fonts.googleapis.com/css2?family=Arimo:wght@400&family=Montserrat:wght@600;700&family=Open+Sans:wght@400;600&display=swap">
<style>
  :root {
    --bg: #000000;
    --card: #2e2f31;
    --card-edge: #3a3b3d;
    --white: #ffffff;
    --soft-white: #e6e6e6;
    --rule: #8a8a8a;
    --green: #7ed320;
    --tagline-grey: #8c8c8c;
  }
  * { margin: 0; padding: 0; box-sizing: border-box; }
  html, body {
    width: 1200px; height: 900px; overflow: hidden;
    background: var(--bg);
  }
  .stage { position: relative; width: 1200px; height: 900px; }
  .card {
    position: absolute;
    width: 458px; height: 280px;
    border-radius: 12px;
    background: linear-gradient(180deg, var(--card-edge) 0%, var(--card) 40%, var(--card) 100%);
  }
  .card--front { left: 137px; top: 265px; }
  .card--back  { left: 625px; top: 268px; }

  .brand { position: absolute; white-space: nowrap; }
  .brand__row { display: flex; align-items: center; }
  .brand__dot { border-radius: 50%; flex: none; }
  .brand__name {
    font-family: "Montserrat", sans-serif;
    font-weight: 700;
    line-height: 1;
  }
  .brand__tagline {
    font-family: "Open Sans", sans-serif;
    font-weight: 600;
    text-transform: uppercase;
    line-height: 1;
  }

  .card--front .brand { left: 38px; top: 124px; width: 183px; }
  .card--front .brand__dot { width: 12px; height: 12px; background: var(--white); margin-right: 8px; }
  .card--front .brand__name { color: var(--white); font-size: 31px; letter-spacing: 1px; }
  .card--front .brand__tagline { color: var(--white); font-size: 8.2px; letter-spacing: 1.1px; margin-top: 9px; }

  .divider {
    position: absolute; left: 239px; top: 70px;
    width: 1px; height: 145px; background: var(--rule);
  }

  .contact { position: absolute; left: 256px; top: 67px; color: var(--white); }
  .contact__name {
    font-family: "Montserrat", sans-serif; font-weight: 600;
    font-size: 16.5px; letter-spacing: 0.2px; line-height: 1.1;
  }
  .contact__title {
    font-family: "Arimo", sans-serif; font-size: 11.5px;
    letter-spacing: 0.4px; color: var(--soft-white); margin-top: 1px;
  }
  .contact__list { list-style: none; margin-top: 13px; }
  .contact__item {
    display: flex; align-items: center;
    font-family: "Arimo", sans-serif; font-size: 13.2px;
    height: 16.6px;
  }
  .contact__icon { width: 12px; height: 12px; margin-right: 5px; flex: none; }
  .contact__address {
    font-family: "Arimo", sans-serif; font-size: 13.2px;
    line-height: 16.6px; margin-top: 9px;
  }

  .card--back .brand { left: 89px; top: 122px; width: 282px; }
  .card--back .brand__row { justify-content: center; }
  .card--back .brand__dot { width: 18px; height: 18px; background: var(--green); margin-right: 12px; }
  .card--back .brand__name { color: var(--green); font-size: 46px; letter-spacing: 2px; }
  .card--back .brand__tagline {
    color: var(--tagline-grey); font-weight: 400;
    font-size: 12.6px; letter-spacing: 2.1px; margin-top: 14px; text-align: center;
  }
</style>
</head>
<body>
<main class="stage">
  <section class="card card--front">
    <div class="brand">
      <div class="brand__row">
        <span class="brand__dot"></span>
        <span class="brand__name">NORVANE</span>
      </div>
      <div class="brand__tagline">IT Solutions for Small Business</div>
    </div>

    <div class="divider"></div>

    <div class="contact">
      <div class="contact__name">DANIEL HART</div>
      <div class="contact__title">MANAGING DIRECTOR</div>
      <ul class="contact__list">
        <li class="contact__item">
          <svg class="contact__icon" viewBox="0 0 24 24" fill="none" stroke="#fff" stroke-width="2.4" stroke-linejoin="round">
            <path d="M5 3h4l2 5-3 2a11 11 0 0 0 6 6l2-3 5 2v4a2 2 0 0 1-2 2A17 17 0 0 1 3 5a2 2 0 0 1 2-2z"/>
          </svg>
          07-3210 5486
        </li>
        <li class="contact__item">
          <svg class="contact__icon" viewBox="0 0 24 24" fill="none" stroke="#fff" stroke-width="2.4">
            <rect x="6" y="2" width="12" height="20" rx="2"/><line x1="10" y1="18" x2="14" y2="18"/>
          </svg>
          07-3210 5486
        </li>
        <li class="contact__item">
          <svg class="contact__icon" viewBox="0 0 24 24" fill="#fff">
            <path d="M2 5h20v14H2z M4 7l8 6 8-6" stroke="#2e2f31" stroke-width="1.6"/>
          </svg>
          hello@norvane.com.au
        </li>
        <li class="contact__item">
          <svg class="contact__icon" viewBox="0 0 24 24" fill="none" stroke="#fff" stroke-width="2">
            <circle cx="12" cy="12" r="10"/><ellipse cx="12" cy="12" rx="4.5" ry="10"/><line x1="2" y1="12" x2="22" y2="12"/>
          </svg>
          www.norvane.com.au
        </li>
      </ul>
      <p class="contact__address">18 Wickham Terrace, Brisbane<br>4000, Australia</p>
    </div>
  </section>

  <section class="card card--back">
    <div class="brand">
      <div class="brand__row">
        <span class="brand__dot"></span>
        <span class="brand__name">NORVANE</span>
      </div>
      <div class="brand__tagline">IT Solutions for Small Business</div>
    </div>
  </section>
</main>
</body>
</html>
```